Trade fair PLAMX business card 7” x 5”

PLAMX exhibits on technology-hospitality trade fair in the UK this year. Therefore we are looking for well-designed marketing card (examples are linked in the bottom). The main role of these materials is to attract receivers to visit our website & find out more about PLAMX solutions.
Preferred used colours: white, various blue tints, black.
The front should contain branding & motto (“Modern beverage stocktaking”). Logotypes are attached.
The back should contain:
(value proposition),
Modern technology solution for beverage stocktaking
Accurate & effective stocktaking
Swift measuring with 99% accuracy makes stocktaking significantly quicker and more cost effective (or cost optimising).
Software solution supported with/by hardware tools
PLAMX system is based on universally accessible platforms - smartphones, PCs, and laptops. Your main measuring tool, smart scale, is delivered by PLAMX.
Smart & simple reporting system
Data availability - everywhere, anytime
Useful functions help stock managing at your bar
(call to action),
Find us on plamx-vend.com and try PLAMX with a one-month free trial.
(promo code)
Claim your 50% off discount with above promo code
Marketing card examples:
https://www.vendrilosa.com/Which-startup-has-the-best-brochure-in-terms-of-design-and-content
PLAMX solution was created to help bar owners, bar managers and head bartenders to make their stocktaking process swift & accurate. Therefore, our product is targeting every business which sells portioned beverages.
Information Technology

```html
<!DOCTYPE html>
<html lang="en">
<head>
<meta charset="utf-8">
<title>PLAMX – Trade Fair Card</title>
<link href="https://fonts.googleapis.com/css2?family=Lato:wght@300;400;700;900&display=swap" rel="stylesheet">
<style>
  :root {
    --ink: #0b0b0b;
    --paper: #ffffff;
    --page: #e9e9e9;
    --text: #1a1a1a;
    --muted: #f3f3f3;
  }
  * { margin: 0; padding: 0; box-sizing: border-box; }
  html, body { width: 1200px; height: 1200px; overflow: hidden; }
  body { background: var(--page); font-family: 'Lato', sans-serif; color: var(--text); position: relative; }

  .card { position: absolute; left: 215px; width: 770px; height: 550px; background: var(--paper); overflow: hidden; }
  .card--front { top: 40px; background: linear-gradient(135deg, #ffffff 55%, #f1f1f1 100%); }
  .card--back { top: 610px; }

  .rule { position: absolute; display: flex; align-items: center; gap: 4px; }
  .rule__bar { height: 100%; background: var(--ink); flex: 1; }
  .rule__ticks { height: 100%; }

  /* front */
  .front-photo { position: absolute; left: 0; top: 67px; width: 438px; height: 397px;
    background: linear-gradient(160deg, #c9cfc6 0%, #e6e2da 35%, #b7b2aa 65%, #d9d3c8 100%); }
  .brand { position: absolute; left: 530px; top: 62px; display: flex; align-items: center; gap: 10px; }
  .brand__mark { width: 14px; height: 14px; background: var(--ink); }
  .brand__name { font-weight: 900; font-size: 54px; line-height: 1; color: var(--ink); letter-spacing: -1px; }
  .front-strip { position: absolute; left: 439px; top: 138px; width: 21px; height: 233px; background: var(--ink); }
  .motto { position: absolute; left: 469px; top: 138px; width: 301px; height: 233px; background: var(--ink); color: var(--paper); padding: 42px 0 0 28px; }
  .motto__top { font-weight: 700; font-size: 47px; line-height: 1; letter-spacing: 0.5px; }
  .motto__mid { font-weight: 300; font-size: 38px; line-height: 1.2; margin-top: 2px; }
  .motto__tag { display: inline-block; background: var(--paper); color: var(--ink); font-weight: 400; font-size: 28px; line-height: 1; padding: 4px 5px 3px; margin-top: 8px; }
  .front-url { position: absolute; left: 535px; top: 390px; font-size: 17px; letter-spacing: 4px; color: var(--ink); }

  /* back */
  .lead { position: absolute; left: 27px; top: 36px; }
  .lead__top { font-weight: 700; font-size: 19px; color: var(--ink); }
  .lead__mid { font-weight: 300; font-size: 24px; line-height: 1.2; }
  .lead__tag { display: inline-block; background: var(--ink); color: var(--paper); font-weight: 700; font-size: 21px; padding: 4px 8px 4px 8px; margin-top: 5px; }
  .point { position: absolute; left: 28px; width: 370px; }
  .point__title { font-weight: 700; font-size: 14px; line-height: 1.2; color: var(--ink); }
  .point__body { font-size: 12px; line-height: 1.35; margin-top: 5px; }
  .features { position: absolute; left: 0; top: 326px; list-style: none; }
  .features li { display: flex; align-items: center; height: 20px; margin-bottom: 12px; font-size: 14px; }
  .features svg { width: 30px; height: 12px; margin-right: 14px; }
  .cta { position: absolute; left: 27px; top: 427px; font-size: 14px; line-height: 1.55; }
  .cta b { font-weight: 700; font-size: 15px; }
  .cta__dot { display: inline-block; width: 11px; height: 11px; border-radius: 50%; background: var(--ink); margin: 0 6px 0 4px; vertical-align: -1px; }
  .cta__small { font-size: 12px; }
  .trial { position: absolute; left: 31px; top: 479px; background: var(--ink); color: var(--paper); font-weight: 700; font-size: 16px; padding: 4px 6px; }
  .back-photo { position: absolute; left: 448px; top: 67px; width: 293px; height: 389px;
    background: linear-gradient(170deg, #7a7a7a 0%, #a8a8a8 40%, #6d6d6d 75%, #8c8783 100%); }
  .promo-tag { position: absolute; left: 490px; top: 42px; background: var(--ink); color: var(--paper); font-size: 12px; padding: 3px 5px; }
  .badge { position: absolute; left: 352px; top: 25px; width: 148px; height: 148px; }
</style>
</head>
<body>

<section class="card card--front" aria-label="Card front">
  <div class="rule" style="left:0;top:45px;width:331px;height:10px;">
    <span class="rule__bar"></span>
    <svg class="rule__ticks" viewBox="0 0 20 10" width="20"><path d="M3 0h3L3 10H0zM9 0h3L9 10H6zM15 0h3l-3 10h-3z" fill="#0b0b0b"/></svg>
  </div>
  <div class="front-photo" role="img" aria-label="Laptop on a wooden table with potted plants"></div>
  <div class="brand"><span class="brand__name">plamx</span></div>
  <div class="front-strip"></div>
  <div class="motto">
    <div class="motto__top">MODERN</div>
    <div class="motto__mid">Beverage</div>
    <div class="motto__tag">STOCKTAKING</div>
  </div>
  <div class="front-url">www.plamx-vend.com</div>
  <div class="rule" style="left:0;top:502px;width:703px;height:12px;">
    <span class="rule__bar"></span>
    <svg class="rule__ticks" viewBox="0 0 26 12" width="26"><path d="M4 0h3L3 12H0zM11 0h3l-4 12H7zM18 0h3l-4 12h-3zM25 0h1l-4 12h-1z" fill="#0b0b0b"/></svg>
  </div>
</section>

<section class="card card--back" aria-label="Card back">
  <div class="lead">
    <div class="lead__top">MODERN TECHNOLOGY</div>
    <div class="lead__mid">Solution for</div>
    <div class="lead__tag">MODERN TECHNOLOGY</div>
  </div>

  <div class="point" style="top:144px;">
    <div class="point__title">ACCURATE &amp; EFFECTIVE STOCKTAKING</div>
    <div class="point__body">Swift measuring with <b>99%</b> accuracy makes stocktaking significantly quicker and more cost effective (or cost optimising).</div>
  </div>
  <div class="point" style="top:220px;">
    <div class="point__title">SOFTWARE SOLUTION SUPPORTED<br>BY HARDWARE TOOLS</div>
    <div class="point__body"><b>PLAMX</b> system is based on universally accessible platforms - smart-phones, PCs, and laptops. Your main measuring tool, smart scale, is delivered by <b>PLAMX</b>.</div>
  </div>

  <ul class="features">
    <li><svg viewBox="0 0 30 12"><path d="M0 0h22l-4 12H0zM24 0h4l-4 12h-4z" fill="#0b0b0b"/></svg>Smart &amp; simple reporting system</li>
    <li><svg viewBox="0 0 30 12"><path d="M0 0h22l-4 12H0zM24 0h4l-4 12h-4z" fill="#0b0b0b"/></svg>Data availability - everywhere, anytime</li>
    <li><svg viewBox="0 0 30 12"><path d="M0 0h22l-4 12H0zM24 0h4l-4 12h-4z" fill="#0b0b0b"/></svg>Useful functions help stock managing at your bar</li>
  </ul>

  <div class="cta">
    Find us on<span class="cta__dot"></span><b>plamx-vend.com</b> and try<br>
    <b>PLAMX</b> <span class="cta__small">with a one-month</span>
  </div>
  <div class="trial">FREE TRIAL</div>

  <div class="rule" style="left:165px;top:489px;width:580px;height:12px;">
    <span class="rule__bar"></span>
    <svg class="rule__ticks" viewBox="0 0 26 12" width="26"><path d="M4 0h3L3 12H0zM11 0h3l-4 12H7zM18 0h3l-4 12h-3zM25 0h1l-4 12h-1z" fill="#0b0b0b"/></svg>
  </div>

  <div class="back-photo" role="img" aria-label="Top view of hands holding a smartphone beside a laptop on a wooden desk"></div>
  <div class="promo-tag">promo code</div>

  <svg class="badge" viewBox="0 0 148 148" aria-label="Claim your 50% off">
    <defs>
      <path id="arcTop" d="M30 74 A44 44 0 0 1 118 74"/>
      <path id="arcBottom" d="M26 82 A48 48 0 0 0 122 82"/>
    </defs>
    <circle cx="74" cy="74" r="73" fill="#fff"/>
    <circle cx="74" cy="74" r="66" fill="#0b0b0b"/>
    <circle cx="74" cy="74" r="56" fill="none" stroke="#fff" stroke-width="1"/>
    <text font-family="Lato, sans-serif" font-size="13" fill="#fff"><textPath href="#arcTop" startOffset="50%" text-anchor="middle">Claim your</textPath></text>
    <text x="74" y="83" font-family="Lato, sans-serif" font-weight="900" font-size="25" fill="#fff" text-anchor="middle">50% OFF</text>
    <text font-family="Lato, sans-serif" font-size="6.5" fill="#fff"><textPath href="#arcBottom" startOffset="50%" text-anchor="middle">discount with above promo code</textPath></text>
  </svg>
</section>

</body>
</html>
```